Harbor Lantern Coffee Company

Logo and coffee packaging design for a new coffee roasting company. Our plan is to small batch, craft roast coffee with $1 for each pound sold donated to non-profit rescue dog operations. Web address will be harborlanterncoffee.example
Prefer a logo with a Jack Russell Terrier or similar dog.....like the little TMV dog or Moxie on the sitcom Pemberton.
Ideally we would have one package/bag for all our coffees with a place to put a sticker for the type coffee (origin, roast style etc) and maybe a sticker for the back or side with the story of a specific rescue dog associated with that roast.
Would like some strong color science based designs to make our product pop on the shelf.

```html
<!DOCTYPE html>
<html lang="en">
<head>
<meta charset="utf-8">
<title>Harbor Lantern Coffee – Bag and Logo</title>
<link rel="stylesheet" href="https://fonts.googleapis.com/css2?family=Oswald:wght@500&family=Passion+One:wght@700&family=Playfair+Display:ital,wght@0,700;1,700&display=swap">
<style>
  :root {
    --bg-top: #6e6e6e;
    --bg-mid: #e6e6e6;
    --bg-bottom: #1c1c1c;
    --bag-brown: #4e2f17;
    --bag-brown-dark: #3a2210;
    --amber: #f0ac3a;
    --amber-deep: #e08b1d;
    --cream: #f3e7b2;
    --cream-light: #f8f0cc;
    --ink: #4a2a12;
    --tan: #c9a06a;
  }
  * { margin: 0; padding: 0; box-sizing: border-box; }
  html, body { width: 1200px; height: 1000px; overflow: hidden; }
  body {
    position: relative;
    background: linear-gradient(180deg, var(--bg-top) 0%, var(--bg-mid) 45%, var(--bg-mid) 62%, var(--bg-bottom) 100%);
    font-family: "Playfair Display", Georgia, serif;
    color: var(--ink);
  }
  .bag { position: absolute; left: 150px; top: 70px; width: 380px; height: 880px; }
  .bag-art { position: absolute; inset: 0; }
  .bag-text { position: absolute; left: 0; width: 380px; text-align: center; }

  .ribbon-brand {
    top: 170px;
    font-family: "Oswald", sans-serif; font-weight: 500;
    font-size: 22px; line-height: 1.1; color: var(--ink);
  }
  .product-name {
    top: 368px;
    font-family: "Passion One", sans-serif; font-weight: 700;
    font-size: 82px; letter-spacing: 1px; color: var(--cream);
    -webkit-text-stroke: 3px var(--ink); paint-order: stroke fill;
  }
  .tagline {
    top: 468px;
    font-style: italic; font-size: 28px; color: var(--ink);
    transform: rotate(-4deg);
  }
  .origin-from { top: 540px; font-size: 26px; }
  .origin-country { top: 570px; font-size: 40px; line-height: 1.1; }
  .origin-grade { top: 616px; font-size: 15px; font-family: "Oswald", sans-serif; }
  .flavor {
    top: 652px; left: 115px; width: 150px;
    font-size: 14px; font-style: italic;
    border: 2px solid var(--ink); border-radius: 18px;
    background: var(--amber); padding: 5px 0;
  }
  .net-weight { top: 752px; font-size: 15px; font-family: "Oswald", sans-serif; }
  .web { top: 774px; font-size: 11px; font-style: italic; }

  .logo { position: absolute; left: 640px; top: 240px; width: 500px; height: 520px; }
  .logo-ring { position: absolute; left: 40px; top: 0; }
  .logo-name {
    position: absolute; left: 170px; top: 210px;
    font-family: "Oswald", sans-serif; font-weight: 500;
    color: var(--ink); text-align: right; line-height: 1.05;
  }
  .logo-name .line-a { display: block; font-size: 64px; }
  .logo-name .line-b { display: block; font-size: 64px; }
  .logo-name .line-c { display: block; font-size: 110px; }
</style>
</head>
<body>
  <div class="bag">
    <svg class="bag-art" width="380" height="880" viewBox="0 0 380 880">
      <defs>
        <linearGradient id="amberGrad" x1="0" y1="0" x2="1" y2="0">
          <stop offset="0" stop-color="var(--amber-deep)"/>
          <stop offset="0.5" stop-color="var(--amber)"/>
          <stop offset="1" stop-color="var(--amber-deep)"/>
        </linearGradient>
      </defs>
      <rect class="bag-body" x="0" y="0" width="380" height="880" fill="var(--bag-brown)"/>
      <rect class="bag-fold" x="0" y="0" width="380" height="40" fill="var(--bag-brown-dark)"/>
      <polygon class="bag-panel" role="img" aria-label="Amber panel with a repeating coffee bean pattern"
        points="80,190 300,190 300,250 320,270 320,430 360,470 360,700 330,730 300,730 300,880 80,880 80,730 50,730 20,700 20,470 60,430 60,270 80,250"
        fill="url(#amberGrad)"/>
      <polygon class="ribbon" points="110,0 270,0 270,330 190,300 110,330" fill="var(--cream)"/>
      <circle class="ribbon-mark" cx="190" cy="70" r="28" fill="none" stroke="var(--tan)" stroke-width="3"/>
      <rect class="origin-label" x="45" y="455" width="290" height="230" rx="30" fill="var(--cream-light)" stroke="var(--ink)" stroke-width="6"/>
    </svg>
    <div class="bag-text ribbon-brand">HARBOR<br>LANTERN<br>COFFEE</div>
    <div class="bag-text product-name">MARLOWE</div>
    <div class="bag-text tagline">craft roast coffee</div>
    <div class="bag-text origin-from">from</div>
    <div class="bag-text origin-country">Colombia</div>
    <div class="bag-text origin-grade">Colombian Supremo</div>
    <div class="bag-text flavor">Jalapeno Chocolate</div>
    <div class="bag-text net-weight">Net Wt. 12 oz. (340g)</div>
    <div class="bag-text web">www.harborlanterncoffee.example</div>
  </div>

  <div class="logo">
    <svg class="logo-ring" width="300" height="300" viewBox="0 0 300 300">
      <circle cx="150" cy="150" r="140" fill="none" stroke="var(--tan)" stroke-width="4"/>
    </svg>
    <div class="logo-name">
      <span class="line-a">HARBOR</span>
      <span class="line-b">LANTERN</span>
      <span class="line-c">COFFEE</span>
    </div>
  </div>
</body>
</html>
```